Bottlecap Decals Inc. NEED DESIGNS FOR THE HOLIDAY STICKERS

We need 6 designs for the HOLIDAY SET of Bottlecap Decals. I have attached some imagery that we like as well as the flagship pack of stickers that were also designed by you AWESOME DESIGNERS!! You are not limited to this imagery, it is only to show you what style we like but remember, YOU ARE THE ARTIST! Each design needs to have a "TO: & FROM:" for people to write in their name and the recipients name. We need designs for the following occasions:

1. HALLOWEEN
2. HAPPY HOLIDAYS (THANKSGIVING, CHRISTMAS, WINTER, LEAVES)
3. ST. PATRICK'S DAY
4. "LET'S CELEBRATE" PATRIOTIC THEME (JULY 4TH, VETERANS DAY, MEMORIAL DAY COMBINED)
5. HAPPY NEW YEAR
6. SUMMER THEME GENERIC

***these 6 designs must fit on one of die cut shapes which are included in the brief***

**PLEASE SUBMIT YOUR IDEA FOR AS MANY DESIGNS AS YOU CAN (PREFERABLY ALL 6). WE NEED 6 DESIGNS SO IF 4 OF YOURS ARE GOOD AND 2 OF ANOTHERS ARE GOOD, YOU WOULD WIN 1ST AND THEY WOULD WIN 2ND.

Font styles to use
Serif
Sans Serif
Decorative
Script

Requirements
Must have
• - lines for "to" and "from"
• - must fit on a die cut shape (provided)
• - must be FUN and colorful!!
Nice to have
• color, imagery, fun!

```html
<!DOCTYPE html>
<html lang="en">
<head>
<meta charset="utf-8">
<title>Let's Celebrate – Holiday Gift Sticker</title>
<link rel="stylesheet" href="https://fonts.googleapis.com/css2?family=Rye&family=Pinyon+Script&display=swap">
<style>
  :root {
    --paper: #ffffff;
    --foil-light: #f3dc7a;
    --foil-mid: #d9b13a;
    --foil-dark: #b8891e;
    --flag-blue: #4f5a92;
    --flag-cream: #d8cfc0;
    --flag-red: #b51e26;
    --rope: #ffffff;
    --title-red: #c2151d;
    --title-shadow: #7d0d12;
    --ink: #1a1a1a;
    --rule: #9a9a9a;
  }
  html, body {
    margin: 0;
    padding: 0;
    width: 1200px;
    height: 1200px;
    overflow: hidden;
    background: var(--paper);
  }
  .sticker {
    display: block;
    width: 1200px;
    height: 1200px;
  }
  .sticker__title {
    font-family: "Rye", serif;
    fill: var(--title-red);
    stroke: var(--title-shadow);
    stroke-width: 2;
    text-anchor: middle;
  }
  .sticker__label {
    font-family: "Pinyon Script", cursive;
    fill: var(--ink);
    font-size: 66px;
  }
  .sticker__field {
    fill: var(--paper);
  }
</style>
</head>
<body>
<svg class="sticker" viewBox="0 0 1500 1500" xmlns="http://www.w3.org/2000/svg">
  <defs>
    <linearGradient id="foil" x1="0" y1="0" x2="1" y2="1">
      <stop offset="0" stop-color="var(--foil-light)"/>
      <stop offset="0.5" stop-color="var(--foil-mid)"/>
      <stop offset="1" stop-color="var(--foil-dark)"/>
    </linearGradient>
    <linearGradient id="flag" x1="0" y1="0" x2="1" y2="0.35">
      <stop offset="0" stop-color="var(--flag-blue)"/>
      <stop offset="0.22" stop-color="var(--flag-blue)"/>
      <stop offset="0.38" stop-color="var(--flag-cream)"/>
      <stop offset="0.58" stop-color="var(--flag-red)"/>
      <stop offset="0.78" stop-color="var(--flag-cream)"/>
      <stop offset="1" stop-color="var(--flag-red)"/>
    </linearGradient>
    <path id="die-cut" d="M465,290 Q760,150 1055,290 L1120,290 Q1120,420 1175,420 L1175,1000 Q1060,1020 1055,1135 Q760,1290 465,1135 Q460,1020 345,1000 L345,420 Q400,420 400,290 Z"/>
  </defs>

  <use class="sticker__edge" href="#die-cut" fill="url(#foil)"/>

  <g transform="translate(760 712) scale(0.93 0.93) translate(-760 -712)">
    <use class="sticker__artwork" href="#die-cut" fill="url(#flag)" role="img" aria-label="Photograph of a stitched American flag with stars and diagonal red and cream stripes"/>
    <use class="sticker__rope-frame" href="#die-cut" fill="none" stroke="var(--rope)" stroke-width="14"/>
  </g>

  <g class="sticker__badge">
    <circle cx="760" cy="590" r="262" fill="none" stroke="var(--paper)" stroke-width="10"/>
    <circle cx="760" cy="590" r="232" fill="none" stroke="var(--paper)" stroke-width="4"/>
    <circle cx="760" cy="590" r="200" fill="var(--paper)"/>
    <rect class="sticker__title-band" x="490" y="545" width="556" height="110" fill="var(--paper)"/>
  </g>

  <text class="sticker__title" x="765" y="518" font-size="122" textLength="250" lengthAdjust="spacingAndGlyphs">LET'S</text>
  <text class="sticker__title" x="766" y="643" font-size="122" textLength="528" lengthAdjust="spacingAndGlyphs">CELEBRATE</text>

  <line x1="585" y1="940" x2="900" y2="940" stroke="var(--rule)" stroke-width="1"/>
  <rect class="sticker__field" x="520" y="955" width="460" height="52"/>
  <rect class="sticker__field" x="520" y="1028" width="455" height="52"/>
  <text class="sticker__label" x="522" y="995">from:</text>
  <text class="sticker__label" x="552" y="1072">to:</text>
</svg>
</body>
</html>
```